hi all

Im after a new age looking business card with my company logo on it

must include these details, I would like the PH and Email to be symbols

If the colours used for card could be kept within the colours used in logo that I have supplied that would be great, if another colour is to be used dark grey would be ok. no light bulbs etc thanks

Details below to be incorporated on card

Damian Holloway

Lic E871302

PH 0219647381

E info@brightvaleelectrical.example.nz

Domestic Commercial Industrial Electricians

```html
<!DOCTYPE html>
<html lang="en">
<head>
<meta charset="utf-8">
<title>Brightvale Electrical – Business Card</title>
<link href="https://fonts.googleapis.com/css2?family=Prompt:wght@400;600&display=swap" rel="stylesheet">
<style>
  :root {
    --backdrop: #1f2022;
    --card-white: #fbfbfa;
    --card-stone: #e5e0db;
    --brand-blue: #2a66b7;
    --ink: #1c1c1c;
    --faint-grey: #e9eaea;
  }
  * { box-sizing: border-box; margin: 0; padding: 0; }
  html, body {
    width: 1200px; height: 800px; overflow: hidden;
    background: var(--backdrop);
    font-family: "Prompt", sans-serif;
  }
  .canvas {
    position: relative; width: 1200px; height: 800px;
  }
  .card {
    position: absolute; left: 330px; width: 540px; height: 310px;
    overflow: hidden;
  }
  .card--front { top: 55px; background: var(--card-white); }
  .card--back { top: 435px; background: var(--card-stone); }

  .front-ring {
    position: absolute; left: 140px; top: 28px;
    width: 260px; height: 240px; border-radius: 50%;
    border: 18px solid var(--faint-grey);
  }
  .wordmark {
    color: var(--brand-blue); font-weight: 600;
    text-transform: uppercase; letter-spacing: 2px; line-height: 1.05;
    text-align: center;
  }
  .wordmark span { display: block; }
  .card--front .wordmark {
    position: absolute; left: 0; right: 0; top: 108px; font-size: 38px;
  }
  .card--front .wordmark .wordmark-sub { font-size: 15px; letter-spacing: 6px; }
  .front-band {
    position: absolute; left: 0; right: 0; bottom: 0; height: 16px;
    background: var(--brand-blue);
  }

  .card--back .wordmark {
    position: absolute; left: 22px; top: 120px; width: 220px;
    font-size: 26px; text-align: left;
  }
  .card--back .wordmark .wordmark-sub { font-size: 11px; letter-spacing: 4px; padding-left: 2px; }
  .contact {
    position: absolute; left: 262px; top: 66px;
    color: var(--ink);
  }
  .contact-name {
    color: var(--brand-blue); font-weight: 600; font-size: 21px;
    text-transform: uppercase; letter-spacing: 1px;
  }
  .contact-licence { font-size: 15px; margin: 2px 0 12px; }
  .contact-line {
    display: flex; align-items: center; gap: 10px;
    font-size: 13px; margin-bottom: 4px;
  }
  .contact-line svg { width: 14px; height: 14px; flex: none; }
  .back-band {
    position: absolute; left: 0; right: 0; bottom: 16px; height: 38px;
    background: var(--brand-blue);
    color: #fff; font-size: 14px;
    display: flex; align-items: center; justify-content: center;
    letter-spacing: .3px;
  }
</style>
</head>
<body>
<main class="canvas">
  <section class="card card--front">
    <div class="front-ring"></div>
    <div class="wordmark">
      <span>Brightvale</span>
      <span class="wordmark-sub">Electrical</span>
    </div>
    <div class="front-band"></div>
  </section>

  <section class="card card--back">
    <div class="wordmark">
      <span>Brightvale</span>
      <span class="wordmark-sub">Electrical</span>
    </div>
    <div class="contact">
      <p class="contact-name">Damian Holloway</p>
      <p class="contact-licence">Lic E871302</p>
      <p class="contact-line">
        <svg viewBox="0 0 16 16" aria-hidden="true"><path d="M4 1.5l2.2 3-1.4 1.6c.9 2 2.5 3.7 4.6 4.7l1.6-1.5 3 2.2-1.3 2.4C7.4 14 2 8.6 1.6 3.2z" fill="none" stroke="var(--brand-blue)" stroke-width="1.2" stroke-linejoin="round"/></svg>
        0219647381
      </p>
      <p class="contact-line">
        <svg viewBox="0 0 16 16" aria-hidden="true"><rect x="1.5" y="3.5" width="13" height="9" fill="none" stroke="var(--brand-blue)" stroke-width="1.2"/><path d="M1.5 3.5L8 9l6.5-5.5" fill="none" stroke="var(--brand-blue)" stroke-width="1.2"/></svg>
        info@brightvaleelectrical.example.nz
      </p>
    </div>
    <div class="back-band">Domestic Commercial Industrial Electricians</div>
  </section>
</main>
</body>
</html>
```